Power Point for new apartment development

I need to create a power point that will help me present a new real estate development. I have put together the powerpoint without any graphics...just the highlights and included a bunch of pics attached to this post. Use them as needed when discussing each slide. I'm really looking to nail this. dont have much time so please work quick and i'll accept the second i like one.
Target Market(s)
investors and financing institutions
Industry/Entity Type
Real Estate
Font styles to use
Serif
Requirements
Must have
- just needs to be awesome... all your choice.
Nice to have
- nothing specific
Should not have
- nothing specific

```html
<!DOCTYPE html>
<html lang="en">
<head>
<meta charset="utf-8">
<title>Property Amenities</title>
<link rel="stylesheet" href="https://fonts.googleapis.com/css2?family=Arimo:wght@700&family=Carlito&display=swap">
<style>
  :root {
    --navy: #243558;
    --title-navy: #243a66;
    --gold: #e6b86a;
    --cream: #f5d7a6;
    --cream-light: #fbe7cb;
    --band-blue: #5f7db3;
    --text: #2a2a2a;
    --photo-warm: #c9a27a;
    --photo-grey: #d8dadd;
    --photo-blue: #b8cde6;
  }
  html, body {
    margin: 0;
    padding: 0;
    overflow: hidden;
  }
  .slide {
    position: relative;
    width: 1200px;
    height: 675px;
    overflow: hidden;
    background: var(--navy);
    font-family: "Carlito", "Calibri", sans-serif;
  }
  .slide-backdrop {
    position: absolute;
    inset: 0;
    width: 1200px;
    height: 675px;
  }
  .slide-title {
    position: absolute;
    left: 0;
    width: 1150px;
    top: 106px;
    margin: 0;
    text-align: center;
    font-family: "Arimo", "Arial", sans-serif;
    font-weight: 700;
    font-size: 51px;
    line-height: 60px;
    color: var(--title-navy);
    letter-spacing: 0.2px;
  }
  .amenity-list {
    position: absolute;
    left: 92px;
    top: 229px;
    margin: 0;
    padding: 0;
    list-style: none;
    font-size: 17.5px;
    line-height: 28.2px;
    color: var(--text);
  }
  .amenity-list li {
    position: relative;
    padding-left: 22px;
  }
  .amenity-list li::before {
    content: "";
    position: absolute;
    left: 0;
    top: 12px;
    width: 4px;
    height: 4px;
    border-radius: 50%;
    background: var(--text);
  }
  .feature-image {
    position: absolute;
    width: 170px;
    height: 107px;
  }
  .feature-image--valet { left: 686px; top: 228px; background: linear-gradient(135deg, #ffffff, #efe6e6); }
  .feature-image--gym { left: 878px; top: 228px; background: linear-gradient(135deg, #ffffff, var(--photo-grey)); }
  .feature-image--network { left: 686px; top: 488px; background: linear-gradient(135deg, #ffffff, var(--photo-blue)); }
  .feature-image--patio { left: 878px; top: 488px; background: linear-gradient(135deg, #8a7a4a, var(--photo-warm)); }
</style>
</head>
<body>
<div class="slide">
  <svg class="slide-backdrop" viewBox="0 0 1280 720" preserveAspectRatio="none" aria-hidden="true">
    <path class="backdrop-cream" fill="var(--cream)"
          d="M0 330 C30 110 220 75 1280 62 L1280 720 L0 720 Z"/>
    <path class="backdrop-cream-light" fill="var(--cream-light)"
          d="M0 420 C200 380 700 370 1280 360 L1280 720 L0 720 Z"/>
    <path class="backdrop-gold-edge" fill="none" stroke="var(--gold)" stroke-width="22"
          d="M-4 345 C26 115 220 75 1290 67"/>
    <path class="backdrop-band-gold" fill="var(--gold)"
          d="M0 668 C400 676 900 664 1280 600 L1280 720 L0 720 Z"/>
    <path class="backdrop-band-blue" fill="var(--band-blue)"
          d="M0 674 C400 682 900 670 1280 608 L1280 720 L0 720 Z"/>
    <rect class="backdrop-band-navy" x="0" y="713" width="1280" height="7" fill="var(--navy)"/>
  </svg>

  <h1 class="slide-title">Property Amenities</h1>

  <ul class="amenity-list">
    <li>24 Hour Valet Services</li>
    <li>State Of The Art Health &amp; Fitness Facility</li>
    <li>Office Suites For Lease</li>
    <li>Micro Convenience Store On Site</li>
    <li>Entire Building is "Smart" operated and managed</li>
    <li>Tenant Office &amp; Conference Room including; Computer, wifi, Print, Fax, Scan, Copy Center</li>
    <li>Outdoor lounges &amp; fireplaces</li>
    <li>Luxury Clubhouse With 73" Smart TV, Patio With Custom Built Outdoor Pizza Oven and Grill, as well as Spa Tub</li>
    <li>Rooftop Landscaped Dog Park and Private Sanctuary Full of Plants and Flowers.</li>
    <li>Wine cellar*</li>
    <li>Tech Lounge</li>
    <li>Dog Park</li>
    <li>Dog wash bay</li>
  </ul>

  <div class="feature-image feature-image--valet" role="img" aria-label="24/7 valet parking sign"></div>
  <div class="feature-image feature-image--gym" role="img" aria-label="Multi-station gym machine"></div>
  <div class="feature-image feature-image--network" role="img" aria-label="Smart building network diagram illustration"></div>
  <div class="feature-image feature-image--patio" role="img" aria-label="Outdoor patio with stone fireplace and lounge chairs"></div>
</div>
</body>
</html>
```